Dental specialist needs a sharp looking letterhead

I am looking for a letterhead to be used to send letters and communication between myself (a dental specialist) and other dentists.
My office is a state of the art dental specialty office.
I need to letterhead to also state:
Gideon R. Whitfield DDS
2847 Birchmont Avenue, Suite K
West Harlow, NY 14391
(716)482-9163
fax: (716)482-9170
whitfieldroot.com (**this email address may change)

i included my logo designs.
thank you

Target Market(s)

dentists

Industry/Entity Type

Communication

Requirements
Must have
• the included logo, whether the vertical or horizontal versions

```html
<!DOCTYPE html>
<html lang="en">
<head>
<meta charset="utf-8">
<title>Keystone Endodontics P.C. – Letterhead</title>
<link rel="stylesheet" href="https://fonts.googleapis.com/css2?family=Questrial&display=swap">
<style>
  :root {
    --backdrop: #d9d9d9;
    --paper: #f7f7f7;
    --ink: #2b2b2b;
    --accent-blue: #1e9ad6;
    --accent-green: #6aaa2e;
  }
  html, body {
    margin: 0;
    width: 1200px;
    height: 968px;
    overflow: hidden;
    background: var(--backdrop);
  }
  .letterhead {
    position: absolute;
    left: 245px;
    top: 24px;
    width: 710px;
    height: 920px;
    background: var(--paper);
    box-shadow: 0 2px 10px rgba(0,0,0,0.15);
    overflow: hidden;
    font-family: "Questrial", "Century Gothic", sans-serif;
    color: var(--ink);
  }
  .brand {
    position: absolute;
    top: 58px;
    right: 80px;
    display: flex;
    align-items: center;
    gap: 10px;
  }
  .brand-dot {
    width: 14px;
    height: 14px;
    border-radius: 50%;
    background: var(--accent-blue);
  }
  .brand-name {
    font-size: 17px;
    letter-spacing: 0.5px;
    color: var(--ink);
  }
  .contact {
    position: absolute;
    left: 44px;
    bottom: 98px;
    font-size: 10.5px;
    line-height: 16px;
    letter-spacing: 0.2px;
  }
  .contact p { margin: 0; }
  .contact .practitioner { text-transform: uppercase; }
  .contact .label { color: var(--accent-blue); }
  .footer-bands {
    position: absolute;
    left: 0;
    bottom: 0;
    width: 710px;
    height: 100px;
  }
</style>
</head>
<body>
  <main class="letterhead">
    <header class="brand">
      <span class="brand-dot"></span>
      <span class="brand-name">Keystone Endodontics P.C.</span>
    </header>

    <footer class="contact">
      <p class="address-line"><span class="practitioner">Gideon R. Whitfield DDS</span> · 2847 Birchmont Avenue, Suite K · West Harlow, NY 14391</p>
      <p class="reach-line"><span class="label">Phone:</span> (716) 482-9163 · <span class="label">Fax:</span> (716) 482-9170 · <span class="label">Email:</span> info@whitfieldroot.com · <span class="label">Web:</span> www.whitfieldroot.com</p>
    </footer>

    <svg class="footer-bands" viewBox="0 0 710 100" preserveAspectRatio="none" aria-hidden="true">
      <path d="M0 0 L150 72 L0 30 Z" fill="var(--accent-blue)"/>
      <path d="M0 52 Q360 70 710 96 L710 100 L0 100 Z" fill="var(--accent-green)"/>
      <path d="M0 30 L150 72 Q70 60 0 52 Z" fill="var(--paper)"/>
    </svg>
  </main>
</body>
</html>
```